Bright Towns Alliance PowerPoint Design Template and Sample Deck

The Bright Towns Alliance is an international organization that seeks to improve the livability, workability and sustainability of the world’s cities.
We seek a versatile PowerPoint design template with 10 slide types plus a “self-documenting” sample deck. Your design will be used in keynote speeches and workshops around the world.
After the contest is completed, we will ask the winning designer to add 10-20 additional slide types for $75 per slide. We also seek a long-term relationship whereby we can request “custom” slides and/or ask the designer to touch up the slides we build to make them better.
FILES. We have uploaded several files:
2. PALETTE. Shows our official colors.
3 LOGOS. Several individual files with different variations of our logo. Some with our motto, some without.
2. SAMPLE SLIDES. Because we were unable to successfully upload our sample deck, we are making it available via this FileCrate link:
https://www.filecrate-example.net/s/q7mrk2tzw9hdn4e/The%20Bright%20Towns%20Alliance%20Design%20Contest%20Notes.docx?dl=0
Target Market(s)
Mayors, department heads, CIOs, senior executives from technology companies
Industry/Entity Type
Information Technology
Colors
Designer to choose colors to be used in the design.
Requirements
Must have
- Please see uploaded Word document for requirements, nice to haves and should not haves and uploaded palette for color preferences.
Nice to have
- see above
Should not have
- see above

```html
<!DOCTYPE html>
<html lang="en">
<head>
<meta charset="utf-8">
<title>Individual Slides 01c</title>
<link rel="stylesheet" href="https://fonts.googleapis.com/css2?family=Roboto:wght@300;900&family=Open+Sans:ital,wght@0,400;0,600;0,700;1,400&display=swap">
<style>
:root{
  --page:#ffffff;
  --stage:#8f8266;
  --heading:#e2b9b9;
  --navy:#0c2a57;
  --blue:#2a55b8;
  --table-head:#4470c8;
  --row:#f1f1f1;
  --ink:#666;
  --light:#f7f7f7;
  --orange:#e84c2a;
  --orange-deep:#d9421f;
  --amber:#ef921f;
  --amber-deep:#dc8318;
  --green:#7a9a30;
  --green-deep:#6d8c2a;
  --map-grey:#d6d6d6;
  --map-white:#eef1f6;
}
*{margin:0;padding:0;box-sizing:border-box}
html,body{width:1200px;height:1200px;overflow:hidden;background:var(--page)}
body{position:relative;font-family:"Open Sans",sans-serif}
.sheet-title{position:absolute;top:54px;left:0;width:1200px;text-align:center;font-family:"Roboto",sans-serif;font-weight:900;font-size:66px;letter-spacing:1px;color:var(--heading)}
.sheet-sub{position:absolute;top:142px;left:0;width:1200px;text-align:center;font-family:"Roboto",sans-serif;font-weight:300;font-size:28px;color:var(--heading)}
.stage{position:absolute;left:67px;top:222px;width:1087px;height:954px;background:var(--stage)}

.slide{position:absolute;width:290px;height:155px;overflow:hidden;box-shadow:2px 3px 5px rgba(0,0,0,.35);background:var(--light)}
.c1{left:131px}.c2{left:470px}.c3{left:810px}
.r1{top:250px}.r2{top:428px}.r3{top:621px}.r4{top:798px}.r5{top:982px}

.section{color:#fff}
.section-orange{background:linear-gradient(90deg,var(--orange-deep),var(--orange))}
.section-amber{background:linear-gradient(90deg,var(--amber-deep),var(--amber))}
.section-green{background:linear-gradient(90deg,var(--green-deep),var(--green))}
.section-label{position:absolute;right:37px;top:72px;text-align:right;font-size:7.5px;font-weight:600;line-height:10px}
.section-label em{display:block;font-weight:400;font-size:5px;line-height:6px;margin-right:-1px}
.section-arrow{position:absolute;left:263px;top:74px;width:10px;height:10px}

.slide-title{position:absolute;top:5px;left:0;width:100%;text-align:center;font-size:10px;font-weight:600;color:var(--blue)}
.dark .slide-title,.photo .slide-title{color:#fff}
.title-dots{position:absolute;top:21px;left:50%;width:12px;margin-left:-6px;border-top:2px dotted var(--blue)}
.dark .title-dots,.photo .title-dots{border-color:#fff}

.footer{position:absolute;left:0;bottom:0;width:100%;height:14px;background:var(--navy);color:#fff;font-size:7px;padding:0 10px;display:flex;justify-content:space-between;align-items:center}
.footer small{font-size:3px;display:flex;align-items:center;gap:3px}
.footer i{display:inline-block;width:6px;height:6px;border-radius:50%;background:var(--blue);font-style:normal;font-size:3px;text-align:center;line-height:6px}

.note{font-size:2.6px;line-height:4px;color:var(--ink);margin-bottom:4px}
.dark .note,.photo .note{color:#e4e9f2;font-style:italic}
.big{font-size:13px;color:var(--blue);font-weight:600}
.mid{font-size:6px;color:var(--ink)}
.check{display:flex;gap:3px;margin-bottom:4px}
.check b{flex:0 0 5px;height:5px;border-radius:50%;background:#4caf50}
.check span{font-size:3.2px;font-weight:700;color:#333;display:block;line-height:4px}
.check .note{margin:0;line-height:3.4px}
.col{position:absolute}

.photo-fill{position:absolute;inset:0;background:linear-gradient(135deg,#b8336f,#d04a92 55%,#ab2c70)}
.stat{position:absolute;top:54px;width:56px;text-align:center;color:#fff;font-size:12px;line-height:14px}
.stat span{display:block;font-size:2.8px;line-height:3.6px;margin-top:1px}
.stat .ico{display:inline-block;width:7px;height:6px;border:1px solid #fff;margin-right:2px;vertical-align:1px}
.s1{left:34px}.s2{left:89px}.s3{left:152px}.s4{left:214px}
.photo .para{position:absolute;left:15px;right:15px;top:102px;text-align:center;line-height:4.6px}

.map{position:absolute;background:linear-gradient(160deg,#dcdcdc,var(--map-grey));border-radius:3px}
.dark .map{background:linear-gradient(160deg,#f4f6fa,var(--map-white))}
.dark{background:var(--navy)}

.table{position:absolute;border-collapse:collapse;font-size:3.2px;color:#444;text-align:center}
.table th{background:var(--table-head);color:#fff;font-weight:600;height:12px;border-right:1px solid #fff}
.table td{height:13px;border-right:1px solid #fff}
.table tr:nth-child(even) td{background:var(--row)}
.table tr:nth-child(odd) td{background:#fff}
.photo-box{position:absolute;background:linear-gradient(135deg,#9a9a9a,#4c4c4c)}
</style>
</head>
<body>
<h1 class="sheet-title">INDIVIDUAL SLIDES - 01c</h1>
<p class="sheet-sub">(Bigger size for more details)</p>
<div class="stage"></div>

<!-- row 1 -->
<section class="slide section section-orange c1 r1">
  <div class="section-label">5 Statistics Heavy<em>Slide Ideas...</em></div>
  <svg class="section-arrow" viewBox="0 0 10 10"><circle cx="5" cy="5" r="4.2" fill="none" stroke="#fff" stroke-width=".8"/><path d="M4 3l2.2 2L4 7" fill="none" stroke="#fff" stroke-width=".8"/></svg>
</section>

<section class="slide c2 r1">
  <div class="slide-title">Your Slide Title Here</div><div class="title-dots"></div>
  <div class="col" style="left:14px;top:34px;width:84px">
    <p class="note">Member towns share open data so that every street, bus and park can work a little better.</p>
    <p class="note">Each number on this page tells one part of that story for the people who live there.</p>
    <div class="check"><b></b><div><span>Enter Your Title Here</span><p class="note">A short line that explains this point to the room in plain words.</p></div></div>
    <div class="check"><b></b><div><span>Enter Your Title Here</span><p class="note">A short line that explains this point to the room.</p></div></div>
    <div class="check"><b></b><div><span>Enter Your Title Here</span><p class="note">A short line that explains this point to the room.</p></div></div>
  </div>
  <div class="col" style="left:112px;top:36px;width:82px">
    <div style="display:flex;gap:4px;align-items:center"><span class="big">66%</span><p class="note" style="margin:0">Of all projects are finished before the date that was set at the start.</p></div>
    <p class="note" style="margin-top:5px">Towns that plan together spend less and finish sooner. Shared tools, shared data and shared staff training help each member grow and keep the gains year after year.</p>
    <div style="display:flex;gap:22px;margin-top:12px"><div class="mid">75%<p class="note">Enter Text</p></div><div class="mid" style="color:var(--blue);font-weight:700">12%<p class="note">Enter Text</p></div></div>
  </div>
  <div class="col" style="left:202px;top:36px;width:80px">
    <div class="mid">45%</div>
    <p class="note">Suitable for all groups, large towns and small ones alike.</p>
    <p class="note">Water, power and transport teams now share one plan, which cuts delays and lets each team see what the others are doing this year.</p>
    <p class="note">Short note on this figure and what it means for the towns that use it.</p>
  </div>
  <div class="footer">Bright Towns Alliance<small>Bright Towns Alliance | Copyright 2017 <i>27</i></small></div>
</section>

<section class="slide photo c3 r1">
  <div class="photo-fill" role="img" aria-label="Audience at a city conference, tinted magenta"></div>
  <div class="slide-title">Your Slide Title Here</div><div class="title-dots"></div>
  <div class="stat s1">101<span>Your Text Here</span></div>
  <div class="stat s2">25150<span>Your Text Here</span></div>
  <div class="stat s3"><b class="ico"></b>672<span>Your Text Here<br>Your subtitle goes here</span></div>
  <div class="stat s4"><b class="ico"></b>980<span>Your Text Here<br>Your subtitle goes here</span></div>
  <p class="note para">These numbers show how far our member towns have come. Shared plans for water, power and transport have saved time and money, and every town that joins brings new ideas to the group. Residents see cleaner streets, faster buses and safer parks, and leaders gain the tools to keep that progress going for many years to come.</p>
  <div class="footer">Bright Towns Alliance<small>Bright Towns Alliance | Copyright 2017 <i>28</i></small></div>
</section>

<!-- row 2 -->
<section class="slide photo c1 r2">
  <div class="photo-fill" role="img" aria-label="Audience at a city conference, tinted magenta"></div>
  <div class="slide-title">Your Slide Title Here</div><div class="title-dots"></div>
  <div class="stat s1">101<span>Your Text Here</span></div>
  <div class="stat s2">25150<span>Your Text Here</span></div>
  <div class="stat s3"><b class="ico"></b>672<span>Your Text Here<br>Your subtitle goes here</span></div>
  <div class="stat s4"><b class="ico"></b>980<span>Your Text Here<br>Your subtitle goes here</span></div>
  <p class="note para">These numbers show how far our member towns have come. Shared plans for water, power and transport have saved time and money, and every town that joins brings new ideas to the group. Residents see cleaner streets, faster buses and safer parks, and leaders gain the tools to keep that progress going for many years to come.</p>
</section>

<!-- row 3 -->
<section class="slide section section-amber c1 r3">
  <div class="section-label">6 World Map<em>Slide Ideas...</em></div>
  <svg class="section-arrow" viewBox="0 0 10 10"><circle cx="5" cy="5" r="4.2" fill="none" stroke="#fff" stroke-width=".8"/><path d="M4 3l2.2 2L4 7" fill="none" stroke="#fff" stroke-width=".8"/></svg>
</section>

<section class="slide c2 r3">
  <div class="slide-title">Your Slide Title Here</div><div class="title-dots"></div>
  <div class="map" role="img" aria-label="Grey world map with blue location pins" style="left:13px;top:41px;width:162px;height:96px"></div>
  <div class="col" style="left:187px;top:35px;width:84px">
    <p class="note">Our members work on every continent. Each pin marks a town that has joined the group and now shares its plans, its data and its lessons with the rest of the network.</p>
    <p class="note">New towns join each year, and each one brings fresh ideas for streets, parks and services.</p>
    <p class="note">Use this map to show where your work is taking place and which regions are growing the fastest. Move the pins to fit your own story.</p>
  </div>
  <div class="footer">Bright Towns Alliance<small>Bright Towns Alliance | Copyright 2017 <i>31</i></small></div>
</section>

<section class="slide c3 r3">
  <div class="slide-title">Your Slide Title Here</div><div class="title-dots"></div>
  <div class="map" role="img" aria-label="Grey world map with blue location pins" style="left:2px;top:29px;width:205px;height:106px"></div>
  <div class="col" style="left:214px;top:47px;width:64px">
    <p class="note">Each pin marks a member town that shares its plans and data.</p>
    <p class="note">New towns join each year and bring fresh ideas for streets, parks and public services to the group.</p>
    <p class="note">Move the pins to show where your own work is taking place.</p>
  </div>
</section>

<!-- row 4 -->
<section class="slide dark c1 r4">
  <div class="slide-title">Your Slide Title Here</div><div class="title-dots"></div>
  <div class="map" role="img" aria-label="White world map with blue and green location pins" style="left:3px;top:34px;width:194px;height:104px"></div>
  <div class="col" style="left:210px;top:58px;width:70px">
    <p class="note">Each pin marks a member town that shares its plans and data.</p>
    <p class="note">New towns join each year and bring fresh ideas for streets, parks and public services to the group.</p>
    <p class="note">Move the pins to show where your own work is taking place.</p>
  </div>
</section>

<section class="slide dark c2 r4">
  <div class="slide-title">Your Slide Title Here</div><div class="title-dots"></div>
  <p class="note" style="position:absolute;left:22px;right:22px;top:30px">Our members work on every continent. Each pin marks a town that has joined the group and now shares its plans, its data and its lessons with the rest of the network. New towns join each year and bring fresh ideas for streets, parks and services.</p>
  <div class="map" role="img" aria-label="White world map with blue location pins" style="left:40px;top:51px;width:179px;height:98px"></div>
</section>

<!-- row 5 -->
<section class="slide section section-green c1 r5">
  <div class="section-label">7 Two Column Table<em>Slide Ideas...</em></div>
  <svg class="section-arrow" viewBox="0 0 10 10"><circle cx="5" cy="5" r="4.2" fill="none" stroke="#fff" stroke-width=".8"/><path d="M4 3l2.2 2L4 7" fill="none" stroke="#fff" stroke-width=".8"/></svg>
</section>

<section class="slide c2 r5">
  <div class="slide-title">Two Column Table Only</div><div class="title-dots"></div>
  <table class="table" style="left:16px;top:30px;width:260px">
    <tr><th>Your Column Title</th><th>Your Column Title</th></tr>
    <tr><td>Enter Your Text</td><td>Enter Your Text</td></tr>
    <tr><td>Enter Your Text</td><td>Enter Your Text</td></tr>
    <tr><td>Enter Your Text</td><td>Enter Your Text</td></tr>
    <tr><td>Enter Your Text</td><td>Enter Your Text</td></tr>
    <tr><td>Enter Your Text</td><td>Enter Your Text</td></tr>
    <tr><td>Enter Your Text</td><td>Enter Your Text</td></tr>
    <tr><td>Enter Your Text</td><td>Enter Your Text</td></tr>
  </table>
  <div class="footer">Bright Towns Alliance<small>Bright Towns Alliance | Copyright 2017 <i>37</i></small></div>
</section>

<section class="slide c3 r5">
  <div class="slide-title">Two Column Table With Image</div><div class="title-dots"></div>
  <table class="table" style="left:16px;top:30px;width:144px">
    <tr><th>Your Column Title</th><th>Your Column Title</th></tr>
    <tr><td>Enter Your Text</td><td>Enter Your Text</td></tr>
    <tr><td>Enter Your Text</td><td>Enter Your Text</td></tr>
    <tr><td>Enter Your Text</td><td>Enter Your Text</td></tr>
    <tr><td>Enter Your Text</td><td>Enter Your Text</td></tr>
    <tr><td>Enter Your Text</td><td>Enter Your Text</td></tr>
    <tr><td>Enter Your Text</td><td>Enter Your Text</td></tr>
    <tr><td>Enter Your Text</td><td>Enter Your Text</td></tr>
  </table>
  <div class="photo-box" role="img" aria-label="Black and white photo of a busy workshop room" style="left:166px;top:30px;width:119px;height:104px"></div>
  <div class="footer">Bright Towns Alliance<small>Bright Towns Alliance | Copyright 2017 <i>38</i></small></div>
</section>
</body>
</html>
```